Landing Page für Persönlichkeitsquiz
Zielgruppe
Persönlichkeitsquiz für Menschen über 40 Jahren die bessere Entscheidungen treffen möchten.
Aufgabenstellung
Landinpage Design plus QUIZ ( 6 Schritte)
Vollständige Projektbeschreibung:
Projektbeschreibung
„Roaming Sideways QUIZ“
roamingsideways.example
- Responsive Design für mobile & website (Most users: mobile)
- Design wird Grundlage für spätere Website
Dieses Quiz wendet sich an Menschen über 40 Jahre, die ihre persönlichen Lebensziele besser erreichen möchten. Bitte denke daran, dass Menschen in unserem Alter schon schlechter sehen – also bitte eine gut lesbare & etwas größere Schrift verwenden!
Auftrag:
QUIZ mit mehreren Runden
Schritte des Quiz:
1. Landingpage
1.1 Video (youtube eingebunden)
1.2 Text
1.3 „Start Quiz“ Button
1.4 „Bekannt aus“ mit Logos von Medien in denen Marv Olden besprochen wurde.
1.5 Testimonials?
QUIZ (Popup)
2. Erste Runde: „Kille“ alle Antworten die Dich nicht interessieren. Total 64 Antworten.
2.1 Text mit Aufgabenbeschreibung „Kille“ alle Antworten die Dich nicht interessieren. Du hast zwei Minuten.“
2.2 Ein Button pro Antwort (wie bei Lernivo)
2.3 Zwei Buttons pro Reihe
2.4 Oben: Progress bar
2.5 Oben: Countdown clock, Restzeit: 2 Minuten
3. Zweite Runde: „Wähle max. 18 Antworten aus die überleben sollen.“
3.1 Text mit Aufgabenbeschreibung „Wähle max. 18 Antworten aus die überleben sollen.“
3.2 Ein Button pro Antwort (wie bei Lernivo)
3.3 Zwei Buttons pro Reihe
3.4 Oben: Progress bar
3.5 Oben: Countdown clock, Restzeit: 60 Sekunden
3.6 Zähler der noch verfügbaren Antworten. Hier: Noch 18, noch 17, noch 16.. etc.
4. Dritte Runde: „Nur 9 Antworten dürfen überleben. Go!“
4.1 Text mit „Nur 9 Antworten dürfen überleben. Go!“
4.2 Ein Button pro Antwort (wie bei Lernivo)
4.3 Zwei Buttons pro Reihe
4.4 Oben: Progress bar
4.5 Oben: Countdown clock, Restzeit 45 ..

```html
<!DOCTYPE html>
<html lang="de">
<head>
<meta charset="utf-8">
<title>Roaming Sideways Quiz</title>
<link rel="stylesheet" href="https://fonts.googleapis.com/css2?family=Open+Sans:wght@400;600;700&display=swap">
<style>
:root{
  --hero-a:#4a1598;
  --hero-b:#2c0f86;
  --hero-text:#6a45b8;
  --press-bg:#633cb4;
  --voices-bg:#5a38a8;
  --card-bg:#6338b8;
  --card-edge:#4f2498;
  --footer-bg:#35138f;
  --ink-dark:#1e1247;
  --accent:#c06ad2;
  --gold:#e0a53a;
  --grey:#6b6b6b;
  --cta-bg:#6a2e63;
  --cta-text:#a24ad3;
}
*{box-sizing:border-box;margin:0;padding:0}
html,body{width:1161px;height:1200px;overflow:hidden}
body{font-family:"Open Sans",Arial,sans-serif;position:relative;background:var(--voices-bg)}
.hero{position:absolute;left:0;top:0;width:1161px;height:550px;background:linear-gradient(110deg,var(--hero-a),var(--hero-b));overflow:hidden}
.brand{position:absolute;left:84px;top:54px;color:var(--hero-text);font-weight:700;font-size:17px;line-height:23px;letter-spacing:.3px}
.nav{position:absolute;top:80px;color:var(--hero-text);font-size:13px}
.nav-lang{left:940px}
.nav-lang svg{vertical-align:middle;margin-left:4px}
.nav-questions{left:1035px}
.hero-title{position:absolute;left:84px;top:192px;color:var(--hero-text);font-weight:700;font-size:25px;line-height:33px}
.hero-copy{position:absolute;left:84px;top:276px;color:var(--hero-text);font-size:12px;line-height:17px}
.hero-cta{position:absolute;left:84px;top:350px;width:120px;height:36px;border-radius:18px;background:var(--cta-bg);color:var(--cta-text);font-weight:700;font-size:13px;line-height:36px;padding-left:14px}
.hero-media{position:absolute;left:992px;top:144px;width:84px;height:270px;background:#5a2290}
.hero-media-cap{position:absolute;left:985px;top:117px;width:32px;height:32px;border-radius:50%;background:#4c1da0}
.modal{position:absolute;left:168px;top:112px;width:825px;height:416px;background:#fff;border-bottom:4px solid var(--accent);box-shadow:0 6px 20px rgba(0,0,0,.25)}
.step{position:absolute;left:563px;top:94px;width:36px;height:36px;border-radius:50%;background:var(--accent);border:2px solid #fff;color:#fff;font-weight:700;font-size:17px;text-align:center;line-height:32px;z-index:2}
.back{position:absolute;left:30px;top:22px;color:var(--gold);font-weight:700;font-size:13px;display:flex;align-items:center;gap:6px}
.timer{position:absolute;left:299px;top:23px;display:flex;align-items:center;gap:6px;font-size:15px}
.timer-value{color:var(--accent);font-weight:700;padding-right:6px;border-right:1px solid #ddd}
.timer-label{color:var(--grey)}
.complete{position:absolute;right:30px;top:22px;color:var(--accent);font-weight:700;font-size:13px}
.progress{position:absolute;left:30px;top:58px;width:764px;height:11px;border-radius:6px;background:var(--accent)}
.task{position:absolute;left:0;top:91px;width:100%;text-align:center}
.task h1{font-size:21px;font-weight:700;color:var(--grey);line-height:28px}
.task p{font-size:15px;color:var(--grey);line-height:22px}
.rank{position:absolute;left:167px;top:162px;display:grid;grid-template-columns:241px 241px;column-gap:9px;row-gap:9px}
.slot{height:47px;border:1px dashed #bbb;color:#bbb;font-weight:700;font-size:22px;text-align:center;line-height:45px}
.answer{height:47px;background:var(--accent);color:#fff;font-size:13px;line-height:47px;padding-left:10px}
.encourage{position:absolute;left:25px;top:342px;font-size:12px;line-height:17px;color:var(--grey)}
.encourage strong{color:var(--accent);display:block}
.next{position:absolute;right:30px;top:360px;color:var(--gold);font-weight:700;font-size:14px;display:flex;align-items:center;gap:6px}
.press{position:absolute;left:0;top:550px;width:1161px;height:254px;background:var(--press-bg);overflow:hidden}
.section-title{position:absolute;left:0;width:100%;text-align:center;color:var(--ink-dark);font-weight:700;font-size:15px}
.section-title::after{content:"";display:block;width:39px;height:3px;background:#4f1fa3;margin:8px auto 0}
.press .section-title{top:38px}
.press-row{position:absolute;left:118px;top:108px;width:928px;display:flex;justify-content:space-between;align-items:center;color:var(--ink-dark);font-weight:700;font-size:19px}
.press-box{display:inline-block;width:12px;height:12px;background:var(--ink-dark);margin-right:6px;vertical-align:middle}
.arrow{position:absolute;top:139px;width:18px;height:18px;border-radius:50%;background:#6b2e62}
.arrow-prev{left:84px}
.arrow-next{left:1059px}
.press-orb{position:absolute;left:1118px;top:25px;width:180px;height:180px;border-radius:50%;background:#3f1a9c}
.voices{position:absolute;left:0;top:804px;width:1161px;height:351px;background:var(--voices-bg);overflow:hidden}
.voices .section-title{top:44px}
.voices-orb{position:absolute;left:-140px;top:50px;width:186px;height:186px;border-radius:50%;background:#4a1ca2}
.card{position:absolute;top:108px;width:324px;height:153px;background:var(--card-bg);border-bottom:4px solid var(--card-edge);padding:18px 16px}
.card-1{left:84px}.card-2{left:418px}.card-3{left:752px}
.avatar{position:absolute;left:16px;top:18px;width:66px;height:66px;border-radius:50%;background:radial-gradient(circle at 50% 40%,#7a5a6a,#3a2440)}
.person{position:absolute;left:100px;top:32px;color:var(--ink-dark)}
.person b{font-size:14px;display:block}
.person span{font-size:10px;font-weight:600}
.person span em{font-style:normal;font-weight:400;margin-right:4px}
.quote-icon{position:absolute;right:14px;top:12px}
.card p{position:absolute;left:16px;top:94px;width:296px;font-size:11px;line-height:15px;color:var(--ink-dark)}
.voices-cta{position:absolute;left:518px;top:290px;width:125px;height:36px;border-radius:18px;background:var(--cta-bg);color:var(--cta-text);font-weight:700;font-size:13px;line-height:36px;text-align:center}
.footer{position:absolute;left:0;top:1155px;width:1161px;height:45px;background:var(--footer-bg);color:#5e3fb0;font-size:11px}
.footer .copy{position:absolute;left:84px;top:15px}
.footer nav{position:absolute;right:90px;top:15px;display:flex;gap:32px}
</style>
</head>
<body>
<header class="hero">
  <div class="brand">ROAMING<br>SIDEWAYS</div>
  <div class="nav nav-lang">Deutsch<svg width="12" height="8" viewBox="0 0 12 8"><path d="M1 1l5 5 5-5" stroke="#6a45b8" stroke-width="1.6" fill="none"/></svg></div>
  <div class="nav nav-questions">Fragen</div>
  <h2 class="hero-title">Herzlich willkommen<br>bei Roaming Sideways</h2>
  <p class="hero-copy">Lorem ipsum dolor sit amet, sadipscing<br>nonumy eirmod tempor invidunt ut<br>aliquyam erat, sed diam voluptua.</p>
  <div class="hero-cta">→ Quiz starten</div>
  <div class="hero-media-cap"></div>
  <div class="hero-media" role="img" aria-label="Eingebettetes Video zum Quiz"></div>
</header>

<section class="modal">
  <div class="step" style="left:394px;top:-18px">5</div>
  <div class="back"><svg width="18" height="18" viewBox="0 0 18 18"><circle cx="9" cy="9" r="9" fill="#e0a53a"/><path d="M10.5 5l-4 4 4 4" stroke="#fff" stroke-width="2" fill="none"/></svg>zurück</div>
  <div class="timer"><svg width="17" height="17" viewBox="0 0 17 17"><circle cx="8.5" cy="8.5" r="7.5" stroke="#c06ad2" stroke-width="1.6" fill="none"/><path d="M8.5 4v5l3 2" stroke="#c06ad2" stroke-width="1.6" fill="none"/></svg><span class="timer-value">00 : 10</span><span class="timer-label">Restzeit: 10 Sekunden</span></div>
  <div class="complete">100 % komplett</div>
  <div class="progress"></div>
  <div class="task"><h1>Sortiere die Antworten nach Relevanz.</h1><p>1= Am wichtigsten, 3= Am unwichtigsten</p></div>
  <div class="rank">
    <div class="slot">1</div><div class="answer">Lorem ipsum dela martime de.</div>
    <div class="slot">2</div><div class="answer">Lorem ipsum dela martime de ma di.</div>
    <div class="slot">3</div><div class="answer">Lorem ipsum dela martime de.</div>
  </div>
  <div class="encourage">Du hast es<strong>fast geschafft!</strong></div>
  <div class="next">Resultat<svg width="18" height="18" viewBox="0 0 18 18"><circle cx="9" cy="9" r="9" fill="#e0a53a"/><path d="M7.5 5l4 4-4 4" stroke="#fff" stroke-width="2" fill="none"/></svg></div>
</section>

<section class="press">
  <div class="press-orb"></div>
  <h2 class="section-title">Bekannt aus</h2>
  <div class="arrow arrow-prev"></div>
  <div class="press-row">
    <span><i class="press-box"></i>Nordfunk</span>
    <span>Le Matinal</span>
    <span>Elbwelle</span>
    <span>kontinent.tv</span>
    <span>radio zwei</span>
    <span>Rheinfunk</span>
    <span><i class="press-box"></i>Tageskanal</span>
  </div>
  <div class="arrow arrow-next"></div>
</section>

<section class="voices">
  <div class="voices-orb"></div>
  <h2 class="section-title">Was sagen andere zum Quiz</h2>
  <article class="card card-1">
    <div class="avatar" role="img" aria-label="Porträtfoto von Fatima Mustermann"></div>
    <div class="person"><b>Fatima Mustermann</b><span><em>aus</em>Berlin</span></div>
    <svg class="quote-icon" width="18" height="18" viewBox="0 0 18 18"><path d="M9 2a7 6 0 1 1-4 11l-3 2 1-4A7 6 0 0 1 9 2z" stroke="#2a1468" stroke-width="1.3" fill="none"/></svg>
    <p>Lorem ipsum dolor sit amet, consetetur sadipscing elitr, sed diam nonumy eirmod tempor invidunt ut labore et dolore magna aliquyam erat, sed diam voluptua.</p>
  </article>
  <article class="card card-2">
    <div class="avatar" role="img" aria-label="Porträtfoto von James Mustermelian"></div>
    <div class="person"><b>James Mustermelian</b><span><em>aus</em>Bayern</span></div>
    <svg class="quote-icon" width="18" height="18" viewBox="0 0 18 18"><path d="M9 2a7 6 0 1 1-4 11l-3 2 1-4A7 6 0 0 1 9 2z" stroke="#2a1468" stroke-width="1.3" fill="none"/></svg>
    <p>Lorem ipsum dolor sit amet, consetetur sadipscing elitr, sed diam nonumy eirmod tempor invidunt ut labore et dolore magna aliquyam erat, sed diam voluptua.</p>
  </article>
  <article class="card card-3">
    <div class="avatar" role="img" aria-label="Porträtfoto von Helga Sonnfeld"></div>
    <div class="person"><b>Helga Sonnfeld</b><span><em>aus</em>Hannover</span></div>
    <svg class="quote-icon" width="18" height="18" viewBox="0 0 18 18"><path d="M9 2a7 6 0 1 1-4 11l-3 2 1-4A7 6 0 0 1 9 2z" stroke="#2a1468" stroke-width="1.3" fill="none"/></svg>
    <p>Lorem ipsum dolor sit amet, consetetur sadipscing elitr, sed diam nonumy eirmod tempor invidunt ut labore et dolore magna aliquyam erat, sed diam voluptua.</p>
  </article>
  <div class="voices-cta">→ Quiz starten</div>
</section>

<footer class="footer">
  <div class="copy">© Roaming Sideways QUIZ</div>
  <nav><span>Impressum</span><span>Datenschutz</span><span>Sitemap</span></nav>
</footer>
</body>
</html>
```